Global Expert Network Firm needs business card design

We need business card design for a new company based in Seoul, South Korea called 'Corwell Insight Partners'. We recruit industry experts covering all countries and connect our client and recruited expert by phone, face-to-face meetings and etc. We are a global expert network firm that is focused on delivering high-quality experts to our clients throughout the world. Our clients include multinational corporations, global consulting firms, private equity firms, venture capital firms, asset management companies.
We have made new logo and please find attachment.(Please use new logo)
Target Market(s)
Global Consulting Firms, Investment Firms, Private Equity Firms, Venture Capital Firms.
Industry/Entity Type
Recruitment
Contact Information for Business Card
We need two Languages (English and Korean Version).
The front is Korean and the back is English version.
[The back] [English]
Company Name: Corwell Insight Partners, Inc.
CEO Name: Daniel Park
Address: #507, Hanbit Bldg, 82 Maebongsan-ro, Dobong-gu, Seoul, 01327, Korea
Tel. +82 2 718 4052
Fax. +82 2 864 1097
Mobile. +82 10 7264 8815
Email: daniel@corwellip.com
Web: www.corwellip.com
[The front] [Korean] => Described in same order as English version.
회사명: 코웰인사이트파트너스(주)
대표이사: 박도현
주소: 서울시 도봉구 매봉산로 82 한빛빌딩 507호
Tel. 02 718 4052
Fax. 02 864 1097
Mobile. 010 7264 8815
Web: www.corwellip.com
Look and feel
Each slider illustrates characteristics of the customer's brand and the style your logo design should communicate.

```html
<!DOCTYPE html>
<html lang="en">
<head>
<meta charset="utf-8">
<title>Corwell Insight Partners – Business Card</title>
<link rel="stylesheet" href="https://fonts.googleapis.com/css2?family=Montserrat:wght@400;500;700&family=Noto+Sans+KR:wght@400;700&display=swap">
<style>
  :root {
    --navy: #1e2a6b;
    --navy-deep: #141c4f;
    --navy-light: #2a3a8a;
    --paper: #fbfbfb;
    --ink: #3a3a3a;
    --ink-light: #eef0f8;
    --backdrop: #e4e5e8;
    --pattern-grey: #e7e7e7;
  }
  * { box-sizing: border-box; margin: 0; padding: 0; }
  html, body { width: 1200px; height: 900px; overflow: hidden; }
  body {
    background: var(--backdrop);
    font-family: "Montserrat", sans-serif;
    position: relative;
  }
  .card {
    position: absolute;
    top: 150px;
    width: 340px;
    height: 600px;
    border-radius: 22px;
    overflow: hidden;
    box-shadow: 0 10px 30px rgba(0,0,0,0.18);
  }
  .card--english { left: 220px; background: var(--paper); }
  .card--korean {
    left: 640px;
    background: linear-gradient(160deg, var(--navy-light) 0%, var(--navy) 55%, var(--navy-deep) 100%);
    color: var(--ink-light);
  }
  .network-pattern {
    position: absolute;
    top: 0; right: 0;
    width: 150px; height: 100%;
  }
  .card--english .network-pattern {
    background: linear-gradient(180deg, rgba(231,231,231,0.9), rgba(231,231,231,0.35));
  }
  .card--korean .network-pattern {
    width: 100%; height: 260px;
    background: linear-gradient(180deg, rgba(255,255,255,0.06), rgba(255,255,255,0));
  }
  .brand {
    position: absolute;
    top: 60px; left: 44px;
    display: flex;
    align-items: center;
    gap: 12px;
  }
  .brand__square {
    width: 34px; height: 34px;
    background: var(--navy);
    flex: none;
  }
  .card--korean .brand__square { background: var(--ink-light); }
  .brand__name {
    font-weight: 500;
    font-size: 19px;
    line-height: 1.2;
    text-transform: uppercase;
    letter-spacing: 0.5px;
    color: var(--navy);
    width: 170px;
  }
  .card--korean .brand__name { color: var(--ink-light); }
  .details {
    position: absolute;
    left: 44px; bottom: 44px;
    font-size: 15px;
    line-height: 1.55;
    color: var(--ink);
  }
  .card--korean .details {
    bottom: auto; top: 320px;
    color: var(--ink-light);
    font-family: "Noto Sans KR", "Montserrat", sans-serif;
  }
  .person__name {
    font-weight: 700;
    font-size: 19px;
    color: var(--navy);
    text-transform: uppercase;
    line-height: 1.2;
  }
  .person__title { font-size: 15px; color: var(--navy); }
  .company-line { font-weight: 700; font-size: 17px; }
  .rule {
    width: 42px; height: 4px;
    background: var(--navy);
    margin: 10px 0 14px;
  }
  .card--korean .rule { background: var(--ink-light); }
  .contact-block { margin-top: 16px; font-family: "Montserrat", sans-serif; }
</style>
</head>
<body>
  <section class="card card--english" aria-label="English side">
    <div class="network-pattern" role="img" aria-label="Faint grey network lines and connection dots"></div>
    <div class="brand">
      <span class="brand__square"></span>
      <span class="brand__name">Corwell Insight Partners</span>
    </div>
    <div class="details">
      <p class="person__name">Daniel Park</p>
      <p class="person__title">Founder &amp; CEO</p>
      <div class="rule"></div>
      <p class="address">#507, Hanbit Bldg, 82<br>Maebongsan-ro, Dobong-gu,<br>Seoul, 01327, Korea</p>
      <p>T: 02 718 4052</p>
      <p>F: 02 864 1097</p>
      <p>M: 010 7264 8815</p>
      <p>daniel@corwellip.com</p>
      <p>www.corwellip.com</p>
    </div>
  </section>

  <section class="card card--korean" aria-label="Korean side" lang="ko">
    <div class="network-pattern" role="img" aria-label="Faint light network lines and connection dots"></div>
    <div class="brand">
      <span class="brand__square"></span>
      <span class="brand__name">Corwell Insight Partners</span>
    </div>
    <div class="details">
      <p class="company-line">회사명: 코웰인사이트파트너스(주)</p>
      <p>대표이사: 박도현</p>
      <div class="rule"></div>
      <p>주소: 서울시 도봉구 매봉산로 82<br>한빛빌딩 507호</p>
      <div class="contact-block">
        <p>T: 02 718 4052</p>
        <p>F: 02 864 1097</p>
        <p>M: 010 7264 8815</p>
        <p>daniel@corwellip.com</p>
        <p>www.corwellip.com</p>
      </div>
    </div>
  </section>
</body>
</html>
```